Auto Mechanic business card

Need a general business card for GearFixer.
Name on card should be 'Roadside Wrench'
Tel # (869) 412 3097
Address is - Palm Lane, Basseterre, St. Kitts
Whatsapp and facebook symbols should be added
On back of card should include services offered
General Repairs
Brakes
Tune Ups
Suspensions
Oil Leaks
Dent repairs
Suspensions
Car Sales
Tyre Repairs
General service
Check Engine Light
Minor Electricals

Target Market(s)

General Population, University students

Industry/Entity Type

Auto Mechanic

Contact Information for Business Card

Roadside Wrench

Requirements
Must have
• 2 Sides

```html
<!DOCTYPE html>
<html lang="en">
<head>
<meta charset="utf-8">
<title>Roadside Wrench – Business Card</title>
<link rel="stylesheet" href="https://fonts.googleapis.com/css2?family=Open+Sans:wght@400;600;800&family=Oswald:wght@600&display=swap">
<style>
  :root {
    --page: #c4c4c4;
    --card-dark: #161616;
    --card-mid: #2b2b2b;
    --red: #e0151b;
    --red-deep: #a10d12;
    --white: #ffffff;
    --muted: #cfcfcf;
    --rule: #9a9a9a;
  }
  * { margin: 0; padding: 0; box-sizing: border-box; }
  html, body { width: 1200px; height: 876px; overflow: hidden; }
  body {
    background: var(--page);
    font-family: "Open Sans", Arial, sans-serif;
    display: flex; align-items: center; justify-content: center; gap: 28px;
  }
  .card {
    position: relative; width: 560px; height: 320px; overflow: hidden;
    background: radial-gradient(ellipse at 35% 30%, var(--card-mid) 0%, var(--card-dark) 70%);
    color: var(--white);
    box-shadow: 0 6px 14px rgba(0,0,0,.35);
  }
  .brand-name {
    font-family: "Open Sans", Arial, sans-serif; font-weight: 800;
    color: var(--white); text-align: center; letter-spacing: .5px;
  }
  .website {
    position: absolute; left: 0; right: 0; text-align: center;
    font-size: 10px; letter-spacing: 5px; color: var(--muted);
  }

  /* services side */
  .card--services .brand-name { position: absolute; top: 22px; left: 0; right: 0; font-size: 38px; }
  .ribbon { position: absolute; top: 82px; left: 118px; width: 324px; height: 44px; }
  .ribbon svg { position: absolute; inset: 0; }
  .ribbon .phone {
    position: relative; display: block; text-align: center; line-height: 44px;
    font-family: "Oswald", Impact, sans-serif; font-weight: 600; font-size: 26px; color: var(--white);
  }
  .address { position: absolute; top: 134px; left: 0; right: 0; text-align: center; font-size: 14px; color: var(--white); }
  .services-heading {
    position: absolute; top: 170px; left: 24px; right: 24px;
    display: flex; align-items: center; gap: 14px;
    font-size: 18px; letter-spacing: .5px;
  }
  .services-heading::before, .services-heading::after { content: ""; flex: 1; height: 1px; background: var(--rule); }
  .services-heading .accent { color: var(--red); }
  .service-columns {
    position: absolute; top: 210px; left: 34px; right: 34px;
    display: grid; grid-template-columns: repeat(4, 1fr); gap: 10px; list-style: none;
  }
  .service-columns ul { list-style: none; }
  .service-columns li { font-size: 11.5px; line-height: 19px; color: var(--white); }
  .service-columns li::before { content: "\00D7"; color: var(--red); font-weight: 800; margin-right: 5px; }
  .card--services .website { bottom: 16px; }

  /* brand side */
  .car-art {
    position: absolute; top: 34px; left: 150px; width: 300px; height: 150px;
    background: radial-gradient(ellipse at 55% 55%, var(--red) 0%, var(--red-deep) 45%, rgba(22,22,22,0) 72%);
    opacity: .8;
  }
  .card--brand .brand-name { position: absolute; top: 188px; left: 0; right: 0; font-size: 42px; }
  .card--brand .website { top: 250px; }
</style>
</head>
<body>

  <section class="card card--services" aria-label="Card back – services">
    <h1 class="brand-name">Roadside Wrench</h1>
    <div class="ribbon">
      <svg viewBox="0 0 324 44" preserveAspectRatio="none" aria-hidden="true">
        <polygon points="0,0 324,0 310,22 324,44 0,44 14,22" fill="var(--red)"/>
      </svg>
      <span class="phone">(869) 412 3097</span>
    </div>
    <p class="address">Palm Lane, Basseterre, St. Kitts</p>
    <h2 class="services-heading"><span>OUR <span class="accent">SERVICES</span></span></h2>
    <div class="service-columns">
      <ul><li>Brakes</li><li>Tune Ups</li><li>Suspensions</li></ul>
      <ul><li>Oil Leaks</li><li>Dent repairs</li><li>Suspensions</li></ul>
      <ul><li>Car Sales</li><li>Tyre Repairs</li><li>General service</li></ul>
      <ul><li>Check Engine Light</li><li>Minor Electricals</li></ul>
    </div>
    <p class="website">www.roadsidewrench.co</p>
  </section>

  <section class="card card--brand" aria-label="Card front – brand">
    <div class="car-art" role="img" aria-label="Red line illustration of a sports car front"></div>
    <h2 class="brand-name">Roadside Wrench</h2>
    <p class="website">www.roadsidewrench.co</p>
  </section>

</body>
</html>
```